Website for Company to help with House Restoration from Hurricane Damage

Crisp, Clean and Professional!

I need a FRONT page for a website. I need it created in photoshop with the layers intact. We DO NOT need the HTML or RBT for the site. Simply the design. Any fonts you use will need to be included if they are not standard. Please make sure any fonts you use in the body of the text are available for use on Google Fonts.

I have attached a word doc that lists the menu items and additional instructions.

A little about the company - after Hurricane Quintessa - RBT developed a system which allows the house to be raised, the Pylonets installed, and the house reset on the Pylonets without the expense of moving the house or driving new pilings. This option can be installed in a matter of days with limited space and at a lower construction cost.

Please refer to the attached musthaves.doc and images that are included.

The main page must incorporate the menu, the attached photos w/ text underneath (text is in the word doc attached), and the text included in the word doc.

Standard footer with contact info as well.

If you have questions please contact us!
Updates

Designs are due by Friday! We will pick one this weekend.  We are unable to change it from 10 days to 5.  Thank you!!!

Target Market(s)

People who lost their homes or businesses due to a hurricane.

Industry/Entity Type

Construction

Requirements
Must have
• See attached musthaves.doc

```html
<!DOCTYPE html>
<html lang="en">
<head>
<meta charset="utf-8">
<title>Reinforced Base Technologies</title>
<link href="https://fonts.googleapis.com/css2?family=Source+Sans+3:wght@400;600;700&display=swap" rel="stylesheet">
<style>
:root{
  --paper:#f1efeb;
  --ink:#555;
  --body:#7d7d7d;
  --olive:#6f8650;
  --olive-light:#9db27a;
  --nav:#55575a;
  --nav-dark:#45474a;
  --footer:#6f8650;
  --hero-top:#8d8494;
  --hero-bottom:#6e6874;
  --white:#fff;
}
*{margin:0;padding:0;box-sizing:border-box}
html,body{width:1200px;height:875px;overflow:hidden}
body{background:var(--paper);font-family:"Source Sans 3",sans-serif;color:var(--ink);position:relative}
.wrap{position:absolute;left:180px;width:840px}
.header{top:0;height:105px}
.brand{position:absolute;left:0;top:30px;display:flex;align-items:center;gap:14px}
.brand-mark{width:60px;height:60px;background:var(--olive)}
.brand-name{font-size:25px;font-weight:400;color:var(--ink)}
.follow{position:absolute;right:4px;top:50px;display:flex;align-items:center;gap:4px;font-size:9px;color:#666}
.follow span{margin-right:2px}
.dot{width:25px;height:25px;border-radius:50%;background:#2f6f9a}
.dot.alt{background:#2b7e98}.dot.sky{background:#43a8d8}.dot.dark{background:#3a3a3a}
.nav{position:absolute;left:0;top:105px;width:1200px;height:43px;background:linear-gradient(#616366,var(--nav))}
.nav ul{list-style:none;position:absolute;left:180px;width:840px;height:43px;display:flex}
.nav li{display:flex;align-items:center;justify-content:center;height:43px;color:var(--white);font-size:10.5px;font-weight:700;text-transform:uppercase}
.nav li.active{background:var(--nav-dark)}
.slider{top:148px;height:378px;overflow:hidden}
.photo{position:absolute;inset:0;background:linear-gradient(var(--hero-top),var(--hero-bottom))}
.arrow{position:absolute;top:154px;width:34px;height:34px;background:rgba(200,200,200,.35)}
.arrow.prev{left:0}.arrow.next{right:0}
.caption{position:absolute;left:0;bottom:0;width:840px;height:80px;background:rgba(35,38,40,.85);display:flex;align-items:baseline;justify-content:center;padding-top:16px;gap:6px}
.caption strong{font-size:35px;font-weight:600;color:var(--olive-light)}
.caption span{font-size:25px;font-weight:400;color:var(--white)}
.shadow{position:absolute;top:526px;left:180px}
.welcome{top:566px;text-align:center;font-size:23px;font-weight:400;color:var(--ink);line-height:34px}
.welcome b{font-weight:400;color:var(--olive);font-size:28px}
.intro{top:616px;font-size:9.3px;line-height:15.4px;color:var(--body)}
.intro p+p{margin-top:15.5px}
.footer{position:absolute;left:0;top:780px;width:1200px;height:95px;background:var(--footer);color:var(--white)}
.footnav{position:absolute;left:184px;top:24px;display:flex;font-size:8px;font-weight:600;text-transform:uppercase}
.footnav li{list-style:none}
.footnav .sep{margin:0 24px;color:var(--white)}
.copy{position:absolute;left:184px;top:47px;font-size:8px;font-weight:600}
.contact{position:absolute;left:795px;top:20px;font-size:8px}
.contact h4{font-size:9px;font-weight:700}
.contact p{margin-top:7px}
.contact .lines{display:flex;gap:12px;margin-top:10px;font-size:8.5px;align-items:center}
.contact .lines span{display:flex;align-items:center;gap:4px}
</style>
</head>
<body>
<header class="wrap header">
  <div class="brand"><div class="brand-mark"></div><div class="brand-name">Reinforced Base Technologies</div></div>
  <div class="follow"><span>FOLLOW US :</span><i class="dot"></i><i class="dot alt"></i><i class="dot sky"></i><i class="dot dark"></i></div>
</header>
<nav class="nav"><ul>
  <li class="active" style="width:117px">Home</li>
  <li style="width:97px">Services</li>
  <li style="width:117px">About Us</li>
  <li style="width:190px">Product Specifications</li>
  <li style="width:190px">Design Documentation</li>
  <li style="width:129px">Contact Us</li>
</ul></nav>
<section class="wrap slider">
  <div class="photo" role="img" aria-label="Photo placeholder: family moment on a beach at sunset"></div>
  <svg class="arrow prev" viewBox="0 0 34 34"><path d="M20 11 L13 17 L20 23Z" fill="#fff"/></svg>
  <svg class="arrow next" viewBox="0 0 34 34"><path d="M14 11 L21 17 L14 23Z" fill="#fff"/></svg>
  <div class="caption"><strong>Rebuild Safer, Stronger,</strong><span>Better to build new lasting memories</span></div>
</section>
<svg class="shadow" width="840" height="24" viewBox="0 0 840 24">
  <defs><radialGradient id="sh" cx="50%" cy="0%" r="50%"><stop offset="0" stop-color="#000" stop-opacity=".35"/><stop offset="1" stop-color="#000" stop-opacity="0"/></radialGradient></defs>
  <ellipse cx="210" cy="0" rx="210" ry="22" fill="url(#sh)"/>
  <ellipse cx="630" cy="0" rx="210" ry="22" fill="url(#sh)"/>
</svg>
<h1 class="wrap welcome"><b>Welcome to RBT</b> Reinforced Base Technologies</h1>
<section class="wrap intro">
  <p>Systems for extending the height of existing piles are not available on today's market. Reinforced Base Technologies, LLC (RBT) has developed two systems to allow for Piles to be extended that provide superior structural support without corrosion and maintenance concerns. We provided two systems, a complete system, Pile Cap Extension Pylonets, and Pile Splice. These two systems allow a home to be raised to by up to 54", higher extensions possible with additional design consideration for lateral support. Shown below is the full Piling Extension system, which connects to the top of the existing pile. The system modular and can be cut to meet specific needs of the home.</p>
  <p>Our Patented Piling system has been designed to withstand the corrosive environment of beach communities. The salt water and windblown sand corrodes unprotected materials, and yes, even stainless steel. Our system utilizes a high strength carbon fiber material that is corrosion proof from salt water and UV proof. The system will not erode, decay or loose strength over time. The system has three installation conditions, for raising a house on existing pilings, repairing damaged pilings, and for connecting new pilings to floor joists in new construction. The three options are generally described here.</p>
</section>
<footer class="footer">
  <ul class="footnav"><li>Home</li><li class="sep">|</li><li>Services</li><li class="sep">|</li><li>About Us</li><li class="sep">|</li><li>Product Specifications</li><li class="sep">|</li><li>Design Documentation</li><li class="sep">|</li><li>Contact Us</li></ul>
  <div class="copy">© COPYRIGHT 2013. REINFORCED BASE TECHNOLOGIES. ALL RIGHT RESERVED</div>
  <div class="contact">
    <h4>REINFORCED BASE TECHNOLOGIES, LLC</h4>
    <p>PO BOX 40512, HARBOR POINT, NJ 08000-0412</p>
    <div class="lines">
      <span><svg width="10" height="14" viewBox="0 0 10 14"><rect x="1" y="1" width="8" height="12" rx="1" fill="none" stroke="#fff"/><circle cx="5" cy="9" r="1.5" fill="#fff"/></svg>(555) 014-2270</span>
      <span><svg width="11" height="8" viewBox="0 0 11 8"><rect x=".5" y=".5" width="10" height="7" fill="none" stroke="#fff"/><path d="M.5 .5 L5.5 4.5 L10.5 .5" fill="none" stroke="#fff"/></svg>sales@reinforcedbase.example</span>
    </div>
  </div>
</footer>
</body>
</html>
```